Logo + Label Design (Men’s Grooming Brand & Product Packaging)

Design a logo and 2 oz pomade label for Brant, a modern men’s grooming brand focused on clean, high-quality, natural ingredients. The design should establish a bold, masculine, minimalist identity that can later extend to products like shaving gel and body wash.

Key Requirements

Create a primary logo for “Brant” and a core label for the 2 oz pomade jar (screw-top).

Use a clean, modern style — masculine, confident, and approachable (think Wendel’s, Valto, Northfield Mill).

Design for 1–2 color screen printing on solid jar colors (white, black, or navy).

Avoid gradients, foil, or embossing. Must work in black & white.

Provide: vector logo, mockup of the 2 oz jar, color palette (CMYK/RGB/HEX), and font specs.

Winning design may lead to future projects (body wash, shave gel, skincare lines).

Font styles to use
Other font styles liked:
• We like the fonts and design concept in the attached mockup.

Requirements
Should not have
• We want to avoid too much writing or busy designs. We want to avoid having graphics/illustrations embedded in the logo if they will cause the brand to look less classy or sophisticated. We also want the design to look simple and all-American (e.g. Pellham and Stroud, Tall Pine, The BRIM, etc). We’d like to give a Kessler & Dunmore vibe that feels classy and high end.

```html
<!DOCTYPE html>
<html lang="en">
<head>
<meta charset="utf-8">
<title>Brant — Hair Pomade &amp; Shave Gel Labels</title>
<link rel="stylesheet" href="https://fonts.googleapis.com/css2?family=Playfair+Display:wght@500&family=Barlow+Condensed:wght@300&family=Cormorant+Garamond:wght@500&display=swap">
<style>
  :root {
    --backdrop: #e4e4e4;
    --label-black: #0c0c0c;
    --brand-blue: #1766d9;
    --ink-light: #e9e9e9;
    --rule-grey: #5e5e5e;
  }
  * { box-sizing: border-box; margin: 0; padding: 0; }
  html, body {
    width: 1200px; height: 741px; overflow: hidden;
    background: var(--backdrop);
  }
  .canvas { position: relative; width: 1200px; height: 741px; }

  .lid-label {
    position: absolute; left: 110px; top: 90px;
    width: 560px; height: 560px; border-radius: 50%;
    background: var(--label-black);
    display: flex; flex-direction: column; align-items: center; justify-content: center;
  }
  .tube-label {
    position: absolute; left: 770px; top: 60px;
    width: 320px; height: 620px;
    background: var(--label-black);
    display: flex; flex-direction: column; align-items: center;
    padding-top: 110px;
  }

  .brand-lockup { display: flex; align-items: center; gap: 14px; }
  .brand-name {
    font-family: "Playfair Display", serif; font-weight: 500;
    color: var(--brand-blue); line-height: 1;
  }
  .product-type {
    font-family: "Barlow Condensed", sans-serif; font-weight: 300;
    color: var(--ink-light); letter-spacing: 0.12em; line-height: 1.05;
  }
  .divider { height: 1px; background: var(--rule-grey); }
  .tagline {
    font-family: "Playfair Display", serif; font-weight: 500;
    color: var(--brand-blue); line-height: 1;
  }
  .hold-spec {
    font-family: "Barlow Condensed", sans-serif; font-weight: 300;
    color: var(--ink-light); letter-spacing: 0.06em;
  }
  .net-weight {
    font-family: "Cormorant Garamond", serif; font-weight: 500;
    color: var(--ink-light);
  }

  .lid-label .brand-name { font-size: 92px; }
  .lid-label .product-type { font-size: 30px; }
  .lid-label .divider { width: 310px; margin: 28px 0 30px; }
  .lid-label .tagline { font-size: 38px; }
  .lid-label .hold-spec { font-size: 30px; margin-top: 14px; }
  .lid-label .net-weight { font-size: 19px; margin-top: 44px; }

  .tube-label .brand-name { font-size: 72px; }
  .tube-label .product-type { font-size: 24px; }
  .tube-label .divider { width: 260px; margin: 36px 0 90px; }
  .tube-label .tagline { font-size: 34px; }
  .tube-label .net-weight { font-size: 18px; margin-top: 40px; }
</style>
</head>
<body>
<main class="canvas">
  <section class="lid-label" aria-label="Brant hair pomade lid label">
    <div class="brand-lockup">
      <span class="brand-name">Brant</span>
      <span class="product-type">HAIR<br>POMADE</span>
    </div>
    <div class="divider"></div>
    <p class="tagline">fresh &amp; clean</p>
    <p class="hold-spec">MEDIUM HOLD – MATTE FINISH</p>
    <p class="net-weight">NET WT 2 oz (57 g)</p>
  </section>

  <section class="tube-label" aria-label="Brant shave gel tube label">
    <div class="brand-lockup">
      <span class="brand-name">Brant</span>
      <span class="product-type">SHAVE<br>GEL</span>
    </div>
    <div class="divider"></div>
    <p class="tagline">fresh &amp; clean</p>
    <p class="net-weight">NET WT 2 oz (57 g)</p>
  </section>
</main>
</body>
</html>
```